TKR Engineering Pty Ltd

I have already had nox welding and fabrication cards made , my business has changed too TKR engineering Pty Ltd so I need my logo changed on the cards
one side have my logo then the other side have what we do.
front side logo and details
owner /operator : Curtis Halvorsen
email: tkr.works@examplemail.net
number: 0491537204
ABN: 52 604 381 927
ACN: 728 391 056
on back have in dot points what we do:
* structural steel erection
* precast panels
* site welding
*steel alteration & repair
* rigging & dogging
*labour hire
Contact Information for Business Card
all details in breif
Look and feel
Each slider illustrates characteristics of the customer's brand and the style your logo design should communicate.

```html
<!DOCTYPE html>
<html lang="en">
<head>
<meta charset="utf-8">
<title>TKR Engineering Pty Ltd — Business Card</title>
<link rel="stylesheet" href="https://fonts.googleapis.com/css2?family=Montserrat:wght@400;500;600;800&family=Oswald:wght@500&display=swap">
<style>
  :root {
    --navy: #0c1c2e;
    --deep-teal: #0a2230;
    --red: #c0402c;
    --white: #ffffff;
    --paper-grey: #f1f1f2;
    --ink: #1b2433;
    --page: #e4e5e7;
  }
  * { box-sizing: border-box; margin: 0; padding: 0; }
  html, body { width: 1200px; height: 1200px; overflow: hidden; }
  body {
    background: var(--page);
    font-family: "Montserrat", Arial, sans-serif;
    display: flex;
    flex-direction: column;
    align-items: center;
    justify-content: center;
    gap: 36px;
  }
  .card {
    width: 900px;
    height: 514px;
    border-radius: 34px;
    position: relative;
    overflow: hidden;
    box-shadow: 0 8px 24px rgba(0,0,0,.18);
  }

  /* Front */
  .card-front {
    background: linear-gradient(180deg, var(--white) 0%, var(--paper-grey) 100%);
    color: var(--ink);
  }
  .contact {
    position: absolute;
    left: 70px;
    top: 110px;
  }
  .contact-name {
    font-size: 40px;
    font-weight: 600;
    letter-spacing: -0.5px;
    text-transform: uppercase;
    color: var(--navy);
    line-height: 1;
  }
  .contact-role {
    font-size: 20px;
    font-weight: 500;
    text-transform: uppercase;
    margin-top: 4px;
  }
  .contact-list { list-style: none; margin-top: 18px; }
  .contact-list li {
    display: flex;
    align-items: center;
    gap: 14px;
    font-size: 24px;
    line-height: 1.3;
  }
  .contact-list svg { width: 22px; height: 22px; flex: none; fill: var(--navy); }
  .contact-reg { font-size: 20px; line-height: 1.25; margin-top: 6px; padding-left: 36px; }

  .wordmark {
    position: absolute;
    display: flex;
    align-items: center;
    gap: 14px;
    font-family: "Montserrat", Arial, sans-serif;
    font-weight: 800;
    text-transform: uppercase;
    line-height: 1.05;
  }
  .wordmark-dot { border-radius: 50%; background: var(--red); flex: none; }
  .card-front .wordmark { right: 60px; top: 110px; font-size: 30px; color: var(--navy); }
  .card-front .wordmark-dot { width: 22px; height: 22px; }

  .services-band {
    position: absolute;
    left: 0; right: 0;
    top: 340px;
    height: 124px;
    background: var(--navy);
    display: flex;
    align-items: center;
    justify-content: flex-end;
    padding-right: 48px;
  }
  .services {
    list-style: none;
    display: grid;
    grid-template-columns: auto auto auto;
    column-gap: 18px;
    row-gap: 6px;
    font-family: "Oswald", "Arial Narrow", sans-serif;
    font-weight: 500;
    font-size: 28px;
    text-transform: uppercase;
    color: var(--white);
    letter-spacing: 0.3px;
  }
  .services li { display: flex; align-items: center; gap: 10px; }
  .services li::before {
    content: "";
    width: 9px; height: 9px;
    border-radius: 50%;
    background: var(--red);
  }

  /* Back */
  .card-back {
    background: linear-gradient(135deg, #0d2a38 0%, var(--deep-teal) 45%, #071a26 100%);
    display: flex;
    align-items: center;
    justify-content: center;
  }
  .card-back .wordmark { position: static; font-size: 50px; color: var(--white); gap: 20px; }
  .card-back .wordmark-dot { width: 34px; height: 34px; }
</style>
</head>
<body>

  <section class="card card-front" aria-label="Card front">
    <div class="contact">
      <p class="contact-name">Curtis Halvorsen</p>
      <p class="contact-role">Owner</p>
      <ul class="contact-list">
        <li>
          <svg viewBox="0 0 24 24" aria-hidden="true"><path d="M6.6 10.8a15.1 15.1 0 0 0 6.6 6.6l2.2-2.2c.3-.3.7-.4 1-.2 1.1.4 2.3.6 3.6.6.6 0 1 .4 1 1V20c0 .6-.4 1-1 1A17 17 0 0 1 3 4c0-.6.4-1 1-1h3.5c.6 0 1 .4 1 1 0 1.3.2 2.5.6 3.6.1.3 0 .7-.2 1z"/></svg>
          0491537204
        </li>
        <li>
          <svg viewBox="0 0 24 24" aria-hidden="true"><path d="M2 5h20v14H2zm2 2v.5l8 5 8-5V7zm0 2.8V17h16V9.8l-8 5z"/></svg>
          tkr.works@examplemail.net
        </li>
      </ul>
      <p class="contact-reg">ABN: 52 604 381 927<br>ACN: 728 391 056</p>
    </div>

    <div class="wordmark">
      <span class="wordmark-dot" aria-hidden="true"></span>
      <span>TKR Engineering<br>Pty Ltd</span>
    </div>

    <div class="services-band">
      <ul class="services">
        <li>Structural steel erection</li>
        <li>Precast panels</li>
        <li>Site welding</li>
        <li>Steel alteration &amp; repair</li>
        <li>Rigging &amp; dogging</li>
        <li>Labour hire</li>
      </ul>
    </div>
  </section>

  <section class="card card-back" aria-label="Card back">
    <div class="wordmark">
      <span class="wordmark-dot" aria-hidden="true"></span>
      <span>TKR Engineering<br>Pty Ltd</span>
    </div>
  </section>

</body>
</html>
```